Fresh look for Client Documents

We have a new software system and it now generates word document reports. We need these tidied up and consistently branded with a stylish corporate theme. We also need to add a "powered by Brimquell" theme to them as the reports are generated by business that use the software so the documents do not exactly 'belong' to their brand. On all of them we need to have the powred by Brimquell PLUS provision for a businesses own logo.
All the documents are generated in Word

```html
<!DOCTYPE html>
<html lang="en">
<head>
<meta charset="utf-8">
<title>Brimquell Report Template</title>
<link href="https://fonts.googleapis.com/css2?family=Poppins:wght@400;500;600;700&display=swap" rel="stylesheet">
<style>
  :root {
    --navy: #232f8c;
    --navy-deep: #1a236f;
    --navy-light: #3a48a8;
    --ink: #2b2b3a;
    --muted: #6b6f80;
    --rule: #c9cbd4;
    --row-grey: #e4e5ea;
    --paper: #ffffff;
    --backdrop: #eef0f3;
  }
  * { box-sizing: border-box; margin: 0; padding: 0; }
  html, body { width: 1200px; height: 2400px; overflow: hidden; }
  body {
    background: var(--backdrop);
    font-family: "Poppins", sans-serif;
    color: var(--ink);
    position: relative;
  }
  .page {
    position: absolute;
    left: 240px;
    width: 720px;
    background: var(--paper);
    overflow: hidden;
  }

  /* Cover */
  .cover { top: 192px; height: 936px; }
  .cover-hero {
    position: absolute; left: 0; top: 0; width: 720px; height: 808px;
    background: linear-gradient(135deg, var(--navy-deep) 0%, var(--navy) 45%, var(--navy-light) 100%);
  }
  .cover-brand {
    position: absolute; left: 72px; top: 88px;
    display: flex; flex-direction: column; align-items: center; gap: 12px;
    color: #fff;
  }
  .cover-brand .mark { width: 44px; height: 44px; background: #fff; }
  .cover-brand .name { font-weight: 600; font-size: 28px; letter-spacing: 1px; line-height: 1; }
  .cover-brand .powered { font-weight: 400; font-size: 14px; letter-spacing: 1px; line-height: 1; opacity: .85; }
  .logo-slot {
    position: absolute; right: 72px; top: 88px; width: 150px; height: 110px;
    border: 2px dashed rgba(255,255,255,.55); border-radius: 8px;
  }
  .cover-code { position: absolute; left: 72px; top: 470px; color: #fff; font-weight: 600; font-size: 28px; letter-spacing: 3px; line-height: 1.2; }
  .cover-title { position: absolute; left: 70px; top: 506px; color: #fff; font-weight: 600; font-size: 58px; line-height: 1.1; }
  .cover-address { position: absolute; left: 72px; top: 578px; color: #fff; font-size: 28px; font-weight: 400; line-height: 1.2; }
  .cover-meta { position: absolute; left: 72px; top: 622px; color: #fff; font-size: 19px; line-height: 32px; }
  .cover-rule { position: absolute; left: 72px; top: 700px; width: 96px; height: 4px; background: #fff; }
  .cover-web { position: absolute; left: 72px; top: 852px; color: var(--navy); font-size: 24px; font-weight: 500; letter-spacing: 1px; line-height: 1.2; }

  /* Form page */
  .form { top: 1192px; height: 948px; }
  .field { position: absolute; left: 32px; width: 628px; border-bottom: 2px solid var(--rule); padding-bottom: 10px; font-size: 24px; }
  .field-building { top: 74px; }
  .field-address { top: 162px; }
  .field-group { top: 268px; }

  .checklist { position: absolute; left: 28px; top: 420px; width: 664px; border-collapse: separate; border-spacing: 0 4px; font-size: 12px; }
  .checklist th { background: var(--navy); color: #fff; font-weight: 600; height: 52px; text-align: center; font-size: 12px; }
  .checklist th:first-child { border-radius: 10px 0 0 10px; }
  .checklist th:last-child { border-radius: 0 10px 10px 0; }
  .checklist td { height: 30px; padding: 0 10px; vertical-align: middle; }
  .checklist .head-row td { font-weight: 600; font-size: 15px; }
  .checklist .shaded td { background: var(--row-grey); }
  .checklist .shaded td:first-child { border-radius: 8px 0 0 8px; }
  .checklist .shaded td:last-child { border-radius: 0 8px 8px 0; }
  .tick { text-align: center; }
  .tick svg { width: 16px; height: 16px; }

  .form-web { position: absolute; left: 32px; top: 882px; color: var(--navy); font-size: 20px; font-weight: 500; letter-spacing: 1px; line-height: 1.2; }
  .form-brand {
    position: absolute; right: 40px; top: 846px;
    display: flex; flex-direction: column; align-items: center; gap: 6px;
    color: var(--navy);
  }
  .form-brand .mark { width: 22px; height: 22px; background: var(--navy); }
  .form-brand .name { font-weight: 600; font-size: 20px; letter-spacing: 1px; line-height: 1; }
  .form-brand .powered { font-weight: 400; font-size: 11px; letter-spacing: 1px; line-height: 1; color: var(--muted); }
</style>
</head>
<body>
  <section class="page cover">
    <div class="cover-hero" role="img" aria-label="Photo of a tall glass office tower in blue tones"></div>
    <div class="cover-brand">
      <span class="mark"></span>
      <span class="name">BRIMQUELL</span>
      <span class="powered">powered by Brimquell</span>
    </div>
    <div class="logo-slot" role="img" aria-label="Space for the business's own logo"></div>
    <div class="cover-code">UPXXXX</div>
    <h1 class="cover-title">Building Name</h1>
    <div class="cover-address">Full Address</div>
    <div class="cover-meta">Strata Group: Strata Group Name<br>Strata Manager: Strata Manager Name</div>
    <div class="cover-rule"></div>
    <div class="cover-web">www.brimquell.com.au</div>
  </section>

  <section class="page form">
    <div class="field field-building">Building Name</div>
    <div class="field field-address">Building Address</div>
    <div class="field field-group">Management Group</div>

    <table class="checklist">
      <colgroup>
        <col style="width:132px"><col style="width:140px"><col style="width:70px">
        <col style="width:55px"><col style="width:55px"><col style="width:55px"><col style="width:157px">
      </colgroup>
      <tr><th></th><th></th><th>Defect Observed?</th><th>Minor</th><th>Moderate</th><th>Major</th><th>Comments</th></tr>
      <tr class="head-row">
        <td>Area</td><td>Item</td>
        <td class="tick"><svg viewBox="0 0 16 16"><rect x="1" y="1" width="14" height="14" fill="none" stroke="#2b2b3a" stroke-width="1.2"/><path d="M4 8l3 3 5-6" fill="none" stroke="#2b2b3a" stroke-width="1.5"/></svg></td>
        <td class="tick"><svg viewBox="0 0 16 16"><rect x="1" y="1" width="14" height="14" fill="none" stroke="#2b2b3a" stroke-width="1.2"/><path d="M4 8l3 3 5-6" fill="none" stroke="#2b2b3a" stroke-width="1.5"/></svg></td>
        <td class="tick"><svg viewBox="0 0 16 16"><rect x="1" y="1" width="14" height="14" fill="none" stroke="#2b2b3a" stroke-width="1.2"/><path d="M4 8l3 3 5-6" fill="none" stroke="#2b2b3a" stroke-width="1.5"/></svg></td>
        <td class="tick"><svg viewBox="0 0 16 16"><rect x="1" y="1" width="14" height="14" fill="none" stroke="#2b2b3a" stroke-width="1.2"/><path d="M4 8l3 3 5-6" fill="none" stroke="#2b2b3a" stroke-width="1.5"/></svg></td>
        <td></td>
      </tr>
      <tr><td>Basement &amp; Internal Car accommodation</td><td>Walls and fire rating capacity</td><td></td><td></td><td></td><td></td><td></td></tr>
      <tr class="shaded"><td></td><td>Gas detection unit</td><td></td><td></td><td></td><td></td><td></td></tr>
      <tr><td></td><td>Roller shutter doors</td><td></td><td></td><td></td><td></td><td></td></tr>
      <tr class="shaded"><td></td><td>Motion Sensors</td><td></td><td></td><td></td><td></td><td></td></tr>
      <tr><td>Bathrooms &amp; Toilets</td><td>Entrances</td><td></td><td></td><td></td><td></td><td></td></tr>
      <tr class="shaded"><td></td><td>Joinery</td><td></td><td></td><td></td><td></td><td></td></tr>
      <tr><td></td><td>Toilet</td><td></td><td></td><td></td><td></td><td></td></tr>
      <tr class="shaded"><td>Elevator</td><td></td><td></td><td></td><td></td><td></td><td></td></tr>
    </table>

    <div class="form-web">www.brimquell.com.au</div>
    <div class="form-brand">
      <span class="mark"></span>
      <span class="name">BRIMQUELL</span>
      <span class="powered">powered by Brimquell</span>
    </div>
  </section>
</body>
</html>
```